Business Card design project for new family-run construction business

We need a logo and business card designed for a new construction company. We want to convey a professional, but approachable image. We hope to be servicing small residential clients as well as large commercial contracts as well.
Our business will employ a single "Hydro excavator" truck, which can be used for multiple purposes: vacuuming up dirt or water, digging holes, clearing sewer blockages and so on.
We are open to different colour schemes, however blue and white, or yellow/green would be good combinations. We are open to multiple colours (2-4), so long as they are complimentary.

EDIT: Let's not put much emphasis on the octopus... unless it's very clear that the arms are actual vacuum hoses, it won't make sense. An octopus on it's own has little to do with our business.

Please also do not use actual photos of hydro-vac trucks. This is not the aesthetic we are going for.

**The logo should instead be: A stylized outline of a hydrovac truck (a line drawing or digital version of a line-drawing). See the two examples in the attached images of hydrovac trucks. I've also included a very crude pen outline as a reference. Please use your artistic discretion and talent (as I clearly have none) to make something that looks much nicer. Thanks for your efforts!**

The front of the card should have the following elements:
Logo
Name: R & T Hydro Excavation and Flushign
Two phone numbers: Direct and Office
Email address
Website
It should also have the name of the employee and their job title
At the bottom of the card it should say (in a noticeable way): "24/7 Emergency Calls Welcome"

The back of the card should have the following elements:
"20 Years Experience"
"A Canadian Family Run Business"
A small maple-leaf logo that is in a similar style to the rest of the card/logos in the bottom right corner of the back of the card. (see attached)

**We have just added a number of business card designs that really appeal to us to offer inspiration.**
Updates

Reason: We have not received designs that hit the mark of what we are looking for. Feedback has been posted, so we would like to provide the designers more time.

Target Market(s)

Commercial and residential customers. As big as large malls and office buildings, as small single-family home owners

Industry/Entity Type

Construction Company

Contact Information for Business Card

We have just added a number of business card designs that really appeal to us to offer inspiration.

Logo
Email address
Website

"20 Years Experience"

Logo Text

R & T Hydro Excavation and Flushing

Font styles to use
Serif
Sans Serif
Other font styles liked:
• Helvetica, Futura, Impact, bold strong, modern fonts that convey a sense of design and style

Colors
0592cd
ec1f27
9bcb3c

Requirements
Must have
• The front of the card should have the following elements:
• Logo
• Name: R & T Hydro Excavation and Flushign
• Two phone numbers: Direct and Office
• Email address
• Website
• It should also have the name of the employee and their job title
• At the bottom of the card it should say (in a noticeable way): "24/7 Emergency Calls Welcome"
• The back of the card should have the following elements:
• "20 Years Experience"
• "A Canadian Family Run Business"
• A small maple-leaf logo that is in a similar style to the rest of the card/logos in the bottom right corner of the back of the card. (see attached)
Nice to have
• The card does not have to be a perfect rectangle. We are open to rounded corners or cut out elements.
• Also embossing, engraving, adding highlighted/glossy layers (spot glass?), or any other effect that will give the card a unique look/feel is more than welcome.
• We would love to have a card that stands out from others and is compelling to look at it, so we are happy to incorporate any sort of modern printing technology to bring out the design.
• Please feel encouraged to be creative and design something unique, especially for this industry.
• Our dream would be if a Scandinavian architect were to go into the construction business and design this business card ;)
Should not have
• Photographs

```html
<!DOCTYPE html>
<html lang="en">
<head>
<meta charset="utf-8">
<title>R &amp; T Hydro Excavation and Flushing – Business Card</title>
<link rel="stylesheet" href="https://fonts.googleapis.com/css2?family=Jost:wght@400;500;700;800&display=swap">
<style>
  :root {
    --backdrop: #eef1f4;
    --paper: #fbfbf8;
    --frame-blue: #3b6ff2;
    --ink: #1d1d1f;
    --label-blue: #3b6ff2;
    --alert-red: #e3191f;
    --white: #ffffff;
  }
  * { box-sizing: border-box; margin: 0; padding: 0; }
  html, body {
    width: 1200px; height: 1200px; overflow: hidden;
    background: var(--backdrop);
    font-family: "Jost", "Futura", sans-serif;
    color: var(--ink);
  }
  .card {
    position: absolute; left: 320px; top: 110px;
    width: 560px; height: 980px;
    background: var(--paper);
  }
  .card-border {
    position: absolute; left: 18px; top: 18px; right: 18px; bottom: 18px;
    background: var(--frame-blue);
  }
  .card-panel {
    position: absolute; left: 70px; top: 70px; right: 70px; bottom: 70px;
    background: var(--paper);
  }
  .brand {
    position: absolute; top: 140px; left: 0; width: 100%;
    text-align: center;
  }
  .brand-mark {
    display: inline-flex; align-items: center; gap: 14px;
    font-weight: 700; font-size: 54px; letter-spacing: 4px; line-height: 1;
  }
  .brand-dot {
    width: 30px; height: 30px; border-radius: 50%;
    background: var(--frame-blue);
  }
  .brand-tagline {
    margin-top: 16px; font-size: 21px; font-weight: 400;
  }
  .person {
    position: absolute; top: 330px; left: 100px; width: 360px;
    text-align: right;
  }
  .person-name { font-size: 32px; line-height: 1; letter-spacing: -0.5px; }
  .person-name strong { font-weight: 800; }
  .person-name span { font-weight: 400; }
  .person-rule { height: 3px; background: var(--ink); margin: 8px 0 8px; }
  .person-title { font-size: 27px; font-weight: 400; padding-right: 40px; }
  .phones {
    position: absolute; top: 500px; left: 100px;
    display: grid; grid-template-columns: auto auto; column-gap: 22px; row-gap: 4px;
    font-size: 27px; line-height: 1.15;
  }
  .phone-label { color: var(--label-blue); font-weight: 700; }
  .web {
    position: absolute; top: 650px; left: 100px;
    font-size: 27px; line-height: 1.25;
  }
  .emergency-band {
    position: absolute; left: 70px; top: 820px; width: 380px; height: 44px;
    background: var(--alert-red); color: var(--white);
    font-weight: 700; font-size: 20px; letter-spacing: 0.5px;
    display: flex; align-items: center; justify-content: center;
  }
</style>
</head>
<body>
  <article class="card">
    <div class="card-border" role="img" aria-label="Decorative blue geometric border around the card"></div>
    <div class="card-panel"></div>

    <header class="brand">
      <div class="brand-mark"><span class="brand-dot"></span>R &amp; T</div>
      <p class="brand-tagline">Hydro Excavation and Flushing</p>
    </header>

    <section class="person">
      <h1 class="person-name"><strong>FIRST</strong> <span>LASTNAME</span></h1>
      <div class="person-rule"></div>
      <p class="person-title">Job Title</p>
    </section>

    <section class="phones">
      <span class="phone-label">Direct</span><span>123-456-7890</span>
      <span class="phone-label">Office</span><span>987-654-3210</span>
    </section>

    <section class="web">
      <p>name@website.com</p>
      <p>www.website.com</p>
    </section>

    <p class="emergency-band">24/7 Emergency Calls Welcome</p>
  </article>
</body>
</html>
```